Business card por a urban DJ, up scale audience target

Need a sober design, modern, conservative colors but i can consider some options, y play rnb, hip hop, EDM and top40.

Business card for contact and personal info, double sided, use logo attrached please; im 42 so i need a card acording to my age an target audience.

Target Market(s)

Adult people, up scale audience

Industry/Entity Type

Music Download

Contact Information for Business Card

Cel (318) 5024471963 www.kelvarodun.com

Requirements
Must have
• open mind
Nice to have
• open mind
Should not have
• DJ

```html
<!DOCTYPE html>
<html lang="en">
<head>
<meta charset="utf-8">
<title>Kelvaro – Business Card</title>
<link rel="stylesheet" href="https://fonts.googleapis.com/css2?family=Open+Sans:wght@400;700;800&display=swap">
<style>
  :root {
    --backdrop: #1f1f1f;
    --card: #ffffff;
    --ink: #231f20;
  }
  html, body {
    margin: 0;
    padding: 0;
    width: 1200px;
    height: 720px;
    overflow: hidden;
    background: var(--backdrop);
  }
  .canvas {
    position: relative;
    width: 1200px;
    height: 720px;
    display: flex;
    align-items: center;
    justify-content: center;
  }
  .card {
    width: 880px;
    height: 503px;
    background: var(--card);
    display: flex;
    flex-direction: column;
    align-items: center;
    font-family: "Open Sans", sans-serif;
    color: var(--ink);
    box-sizing: border-box;
    padding-top: 150px;
  }
  .brand {
    display: flex;
    align-items: center;
    gap: 18px;
  }
  .brand-mark {
    width: 30px;
    height: 30px;
    background: var(--ink);
  }
  .brand-name {
    font-size: 76px;
    font-weight: 800;
    letter-spacing: 6px;
    line-height: 1;
  }
  .contact {
    margin-top: 60px;
    display: flex;
    flex-direction: column;
    align-items: center;
    gap: 8px;
  }
  .phone-icon {
    width: 22px;
    height: 22px;
    display: block;
  }
  .phone, .web {
    font-size: 20px;
    font-weight: 400;
    letter-spacing: 0.3px;
    line-height: 1.3;
  }
  .web strong { font-weight: 700; }
</style>
</head>
<body>
  <main class="canvas">
    <section class="card">
      <div class="brand">
        <span class="brand-mark"></span>
        <span class="brand-name">KELVARO</span>
      </div>
      <div class="contact">
        <svg class="phone-icon" viewBox="0 0 22 22" aria-hidden="true">
          <rect width="22" height="22" rx="2" fill="#231f20"/>
          <path d="M4.5 9.5c0-2.2 2.9-3.5 6.5-3.5s6.5 1.3 6.5 3.5l-2.3 0.6-0.7-1.8c-1-0.3-2.2-0.4-3.5-0.4s-2.5 0.1-3.5 0.4l-0.7 1.8z" fill="#fff"/>
          <path d="M7.5 11h7l1.8 5.5h-10.6z" fill="#fff"/>
          <circle cx="11" cy="13.6" r="1.4" fill="#231f20"/>
        </svg>
        <div class="phone">(318) 5024471963</div>
        <div class="web">www.<strong>kelvarodun</strong>.com</div>
      </div>
    </section>
  </main>
</body>
</html>
```